stationery for law firm in los angeles, CA
letterhead, envelope, business cards
stationery for law firm in los angeles, CA - Law
Creative Brief
Use specific fonts
I like these for example:Mercury,. Minion, Miller, Adobe Garamond, Sabon. Just examples,not required
Professional
Nadia Carrow
Attorney at Law
22817 Halvern Blvd. Suite 2600 Dellmont Park, CA 90268
Nadia@carrowlegal.test
www.carrowlegal.test
Please can you add Law Offices of Nadia L. Carrow on the stationery

```html
<!DOCTYPE html>
<html lang="en">
<head>
<meta charset="utf-8">
<title>Law Offices of Nadia L. Carrow — Stationery</title>
<link rel="stylesheet" href="https://fonts.googleapis.com/css2?family=EB+Garamond:wght@400&family=Arimo:wght@400&display=swap">
<style>
  :root {
    --backdrop: #8c8c8c;
    --paper: #ffffff;
    --ink: #2e2e2e;
    --rule: #6a6a6a;
    --window: #e4e4e4;
    --window-edge: #bdbdbd;
  }
  * { margin: 0; padding: 0; box-sizing: border-box; }
  html, body { width: 1200px; height: 854px; overflow: hidden; }
  body {
    background: var(--backdrop);
    position: relative;
    font-family: "Arimo", Arial, sans-serif;
    color: var(--ink);
  }
  .sheet {
    position: absolute;
    background: var(--paper);
    overflow: hidden;
    box-shadow: 0 1px 3px rgba(0,0,0,0.25);
  }
  .top-rule { position: absolute; left: 0; right: 0; height: 2px; background: var(--rule); }
  .wordmark {
    position: absolute;
    font-family: "EB Garamond", Garamond, serif;
    font-weight: 400;
    color: var(--ink);
    line-height: 1;
    white-space: nowrap;
  }
  .footer-line {
    position: absolute;
    font-family: "EB Garamond", Garamond, serif;
    color: var(--ink);
    white-space: nowrap;
  }

  /* Letterhead */
  .letterhead { left: 19px; top: 19px; width: 581px; height: 797px; }
  .letterhead .top-rule { top: 128px; left: 44px; right: 44px; height: 1px; }
  .letterhead .wordmark { left: 44px; top: 84px; font-size: 27px; }
  .letterhead .masthead-contact {
    position: absolute; left: 395px; top: 22px;
    font-size: 7.5px; line-height: 11px;
  }
  .letterhead .masthead-contact .rows { margin-top: 6px; }
  .letterhead .masthead-contact .row { display: flex; align-items: center; gap: 5px; }
  .letterhead .masthead-contact svg { width: 7px; height: 7px; }
  .letter-body {
    position: absolute; left: 44px; top: 161px; width: 456px;
    font-size: 11.6px; line-height: 18.4px;
  }
  .letter-body p + p { margin-top: 18px; }
  .letterhead .footer-line { left: 125px; bottom: 18px; font-size: 9px; }

  /* Business card */
  .card { left: 619px; top: 139px; width: 562px; height: 348px; }
  .card .top-rule { top: 44px; }
  .card .wordmark { left: 84px; top: 108px; font-size: 32px; }
  .card .address {
    position: absolute; left: 84px; top: 176px;
    font-size: 11.5px; line-height: 16px;
  }
  .card .contact-list { position: absolute; left: 84px; top: 232px; list-style: none; }
  .card .contact-list li {
    display: flex; align-items: center; gap: 12px;
    font-size: 11.5px; line-height: 19px;
  }
  .card .contact-list svg { width: 13px; height: 13px; flex: none; }

  /* Envelope */
  .envelope { left: 523px; top: 516px; width: 658px; height: 288px; }
  .envelope .top-rule { top: 20px; }
  .envelope .wordmark { left: 209px; top: 52px; font-size: 30px; }
  .address-window {
    position: absolute; left: 420px; top: 100px; width: 218px; height: 112px;
    background: var(--window); border: 1px solid var(--window-edge); border-radius: 6px;
  }
  .envelope .footer-line { left: 360px; bottom: 12px; font-size: 9px; }
</style>
</head>
<body>

<section class="sheet letterhead" aria-label="Letterhead">
  <div class="top-rule"></div>
  <div class="wordmark">Law Offices of Nadia Carrow</div>
  <div class="masthead-contact">
    <div>22817 Halvern Blvd. Suite 2600</div>
    <div>Dellmont Park, CA 90268</div>
    <div class="rows">
      <div class="row"><svg viewBox="0 0 10 10"><path d="M2 1 L4 1 L5 3 L4 4 Q5 6 6 6 L7 5 L9 6 L9 8 Q6 9 3 6 Q1 4 2 1Z" fill="var(--ink)"/></svg>(818) 555 0147</div>
      <div class="row"><svg viewBox="0 0 10 10"><rect x="2" y="1" width="6" height="3" fill="none" stroke="var(--ink)"/><rect x="1" y="4" width="8" height="4" fill="var(--ink)"/></svg>(310) 555 0193</div>
      <div class="row"><svg viewBox="0 0 10 10"><rect x="1" y="2" width="8" height="6" fill="none" stroke="var(--ink)"/><path d="M1 2 L5 5 L9 2" fill="none" stroke="var(--ink)"/></svg>Nadia@carrowlegal.test</div>
      <div class="row"><svg viewBox="0 0 10 10"><circle cx="5" cy="5" r="4" fill="none" stroke="var(--ink)"/><path d="M1 5 H9 M5 1 Q2 5 5 9 Q8 5 5 1" fill="none" stroke="var(--ink)" stroke-width="0.7"/></svg>www.carrowlegal.test</div>
    </div>
  </div>
  <div class="letter-body">
    <p>Lorem ipsum dolor sit amet, consectetur adipiscing elit. Aliquam gravida tellus at justo vehicula lacinia. Curabitur ac dolor felis. Nulla ac ligula a elit ornare posuere eget convallis quam. Etiam quis dapibus est. Suspendisse commodo libero sit dui convallis mattis. Pellentesque nisi urna, molestie sed ultrices eget, convallis malesuada mauris. Sed fringilla, justo ut vestibulum aliquet, felis odio vehicula mauris, eu elementum magna dolor quis dolor. Vivamus quam ipsum, placerat vitae lorem eget, tincidunt volutpat augue. Donec vel odio erat. Aliquam viverra metus vitae posuere elementum.</p>
    <p>Class aptent taciti sociosqu ad litora torquent per conubia nostra, per inceptos himenaeos. Praesent mi lacus, ultrices et est sit amet, ullamcorper sollicitudin metus. Vestibulum ante ipsum primis in faucibus orci luctus et ultrices posuere cubilia. Curae; Fusce eget facilisis nisi. Proin eget nisi quis nulla. Cras id faucibus lorem. Praesent volutpat aliquet posuere. Donec condimentum, ligula vitae pharetra hendrerit, ipsum metus viverra erat, et bibendum nulla massa non mauris. Nunc adipiscing eleifend ante, eget placerat enim tincidunt et. Aenean sollicitudin dolor quam, id rhoncus felis semper facilisis. Vivamus augue ante, pulvinar ac condimentum eget, iaculis convallis elit.</p>
    <p>Sed porttitor lorem non diam tempor tempor. Donec at purus sed dolor venenatis rutrum et in nisl. Nunc sagittis quam in faucibus rutrum. Aenean cursus est mauris, nec imperdiet mi scelerisque nec. Donec dictum vulputate odio malesuada porttitor.</p>
  </div>
  <div class="footer-line">Law Offices of Nadia L. Carrow on the stationery</div>
</section>

<section class="sheet card" aria-label="Business card">
  <div class="top-rule"></div>
  <div class="wordmark">Law Offices of Nadia Carrow</div>
  <div class="address">
    <div>22817 Halvern Blvd. Suite 2600</div>
    <div>Dellmont Park, CA 90268</div>
  </div>
  <ul class="contact-list">
    <li><svg viewBox="0 0 10 10"><path d="M2 1 L4 1 L5 3 L4 4 Q5 6 6 6 L7 5 L9 6 L9 8 Q6 9 3 6 Q1 4 2 1Z" fill="var(--ink)"/></svg>(818) 555 0147</li>
    <li><svg viewBox="0 0 10 10"><rect x="2" y="1" width="6" height="3" fill="none" stroke="var(--ink)"/><rect x="1" y="4" width="8" height="4" fill="var(--ink)"/></svg>(310) 555 0193</li>
    <li><svg viewBox="0 0 10 10"><rect x="1" y="2" width="8" height="6" fill="none" stroke="var(--ink)"/><path d="M1 2 L5 5 L9 2" fill="none" stroke="var(--ink)"/></svg>Nadia@carrowlegal.test</li>
    <li><svg viewBox="0 0 10 10"><circle cx="5" cy="5" r="4" fill="none" stroke="var(--ink)"/><path d="M1 5 H9 M5 1 Q2 5 5 9 Q8 5 5 1" fill="none" stroke="var(--ink)" stroke-width="0.7"/></svg>www.carrowlegal.test</li>
  </ul>
</section>

<section class="sheet envelope" aria-label="Envelope">
  <div class="top-rule"></div>
  <div class="wordmark">Law Offices of Nadia Carrow</div>
  <div class="address-window" aria-hidden="true"></div>
  <div class="footer-line">Law Offices of Nadia L. Carrow on the stationery</div>
</section>

</body>
</html>
```